Wildlife photographer Website

The website is to be a "resume" of pictures and awards won by Nora. Lean heavy to outdoor wildlife.
She will post articles and have ability to interact with fans.

I will add some of her pictures tonight,

Target Market(s)

Terra Quarterly .....anyone looking to hire a wildlife photographer.

Industry/Entity Type

Professional Photography

Contact Information for Business Card

Nora Falkett
4817 Maple Hollow Lane
Columbia MD 21078
443-581-2094
Nora@FernOwlPix.com

Coding

Coded - Design and coding required

Number of Pages Required

5+ page

Requirements
Must have
• New Logo
Nice to have
• Nature, and eye catching graphics

```html
<!DOCTYPE html>
<html lang="en">
<head>
<meta charset="utf-8">
<title>Nora Falkett — Wildlife Photography</title>
<link href="https://fonts.googleapis.com/css2?family=Poppins:wght@300;400;500;600&display=swap" rel="stylesheet">
<style>
:root{
  --bg:#0e0e0e;
  --bg-alt:#1d1d1d;
  --footer-bar:#1a1a1a;
  --gold:#c9a443;
  --white:#ffffff;
  --text:#d8d8d8;
  --muted:#8a8a8a;
  --faint:#5a5a5a;
  --line:#444;
}
*{margin:0;padding:0;box-sizing:border-box}
html,body{width:1200px;height:2756px;overflow:hidden;background:var(--bg)}
body{position:relative;font-family:'Poppins',sans-serif;color:var(--text)}
.abs{position:absolute}
.brand{font-family:'Poppins',sans-serif;font-weight:400;font-size:22px;color:var(--white);letter-spacing:.5px}
/* header */
.site-header{left:0;top:0;width:1200px;height:71px;background:var(--bg)}
.site-header .brand{left:128px;top:20px}
.nav{top:23px;left:568px;display:flex;gap:0;font-size:12px;color:var(--text)}
.nav a{color:var(--text);text-decoration:none;padding:5px 13px;border:1px solid transparent;border-radius:2px}
.nav a.active{border-color:#3a3a3a;color:var(--white)}
.btn-quote{left:972px;top:21px;width:100px;height:29px;background:var(--gold);color:var(--white);font-size:9.5px;font-weight:600;display:flex;align-items:center;justify-content:center;border-radius:2px}
/* hero */
.hero{left:0;top:71px;width:1200px;height:431px;background:linear-gradient(180deg,#5d7f8e 0%,#6f8a77 45%,#8a7a5e 75%,#5b4a3a 100%)}
.slide-arrows{left:128px;top:467px;display:flex;gap:4px}
.arrow-box{width:21px;height:21px;background:var(--white);display:flex;align-items:center;justify-content:center;border-radius:2px}
.arrow-box.dim{background:#555}
/* contact bar */
.contact-bar{left:0;top:502px;width:1200px;height:48px;font-size:12px;color:var(--muted)}
.contact-item{top:16px;display:flex;align-items:center;gap:9px}
.socials{display:flex;gap:18px;align-items:center}
.social-dot{width:13px;height:13px;border:1.5px solid var(--muted);border-radius:50%}
/* sections */
.section-title{font-size:27px;font-weight:500;color:var(--white)}
.title-rule{height:1px;background:var(--line)}
.photo{width:301px;height:300px}
.btn-outline{width:107px;height:29px;border:1px solid #3d3d3d;color:var(--muted);font-size:9.5px;display:flex;align-items:center;justify-content:center;border-radius:2px}
.blogs-band{left:0;top:1430px;width:1200px;height:635px;background:var(--bg-alt)}
.post-title{color:var(--white);font-weight:500}
.meta{display:flex;align-items:center;gap:6px;font-size:10px;color:var(--muted)}
.meta .sep{width:1px;height:12px;background:#3a3a3a;margin:0 20px}
.read{color:var(--muted)}
.read.on{color:var(--gold)}
/* form */
.field{background:var(--white);border-radius:2px;display:flex;align-items:center;gap:9px;padding:0 15px;font-size:10.5px;color:#888}
.field.area{align-items:flex-start;padding-top:11px}
.btn-submit{left:550px;top:2351px;width:99px;height:29px;background:var(--gold);color:var(--white);font-size:9.5px;font-weight:500;display:flex;align-items:center;justify-content:center;border-radius:2px}
/* footer */
.footer-head{font-size:17px;color:#6e6e6e}
.footer-links{font-size:12px;color:var(--white);line-height:27.5px;list-style:none}
.footer-links .on{color:var(--gold);text-decoration:underline}
.footer-contact{font-size:12px;color:var(--white)}
.footer-contact li{list-style:none;display:flex;align-items:center;gap:11px;height:38px}
.footer-bar{left:0;top:2718px;width:1200px;height:38px;background:var(--footer-bar)}
</style>
</head>
<body>

<header class="site-header abs">
  <div class="brand abs">Nora Falkett</div>
  <nav class="nav abs">
    <a class="active">Home</a><a>About us</a><a>Photo Gallery</a><a>Blogs</a><a>Contact Us</a>
  </nav>
  <div class="btn-quote abs">GET A QUOTE</div>
</header>

<div class="hero abs" role="img" aria-label="Leopard resting on a rock against a blurred blue-green forest"></div>
<div class="slide-arrows abs">
  <div class="arrow-box"><svg width="8" height="10" viewBox="0 0 8 10"><path d="M6 1 2 5l4 4" stroke="#222" stroke-width="1.6" fill="none"/></svg></div>
  <div class="arrow-box"><svg width="8" height="10" viewBox="0 0 8 10"><path d="M2 1l4 4-4 4" stroke="#222" stroke-width="1.6" fill="none"/></svg></div>
</div>

<div class="contact-bar abs">
  <div class="contact-item abs" style="left:128px">
    <svg width="14" height="10" viewBox="0 0 14 10"><rect width="14" height="10" fill="var(--gold)"/><path d="M0 0l7 6 7-6" stroke="#0e0e0e" stroke-width="1.2" fill="none"/></svg>
    nora@fernowlpix.com
  </div>
  <div class="contact-item abs" style="left:333px">
    <svg width="13" height="13" viewBox="0 0 24 24"><path fill="var(--gold)" d="M6.6 10.8a15 15 0 0 0 6.6 6.6l2.2-2.2c.3-.3.7-.4 1-.2 1.1.4 2.3.6 3.6.6.6 0 1 .4 1 1V20c0 .6-.4 1-1 1A17 17 0 0 1 3 4c0-.6.4-1 1-1h3.5c.6 0 1 .4 1 1 0 1.3.2 2.5.6 3.6.1.3 0 .7-.2 1z"/></svg>
    443-581-2094
  </div>
  <div class="socials abs" style="left:960px;top:17px">
    <span class="social-dot"></span><span class="social-dot" style="border-color:var(--gold)"></span><span class="social-dot"></span><span class="social-dot"></span>
  </div>
</div>

<!-- Photo gallery -->
<div class="title-rule abs" style="left:0;top:606px;width:113px"></div>
<h2 class="section-title abs" style="left:126px;top:587px">Photo Gallery</h2>
<div class="abs" style="left:1020px;top:598px;display:flex;gap:4px">
  <div class="arrow-box dim"><svg width="8" height="10" viewBox="0 0 8 10"><path d="M6 1 2 5l4 4" stroke="#777" stroke-width="1.6" fill="none"/></svg></div>
  <div class="arrow-box"><svg width="8" height="10" viewBox="0 0 8 10"><path d="M2 1l4 4-4 4" stroke="#222" stroke-width="1.6" fill="none"/></svg></div>
</div>
<div class="photo abs" style="left:128px;top:665px;background:linear-gradient(160deg,#9fb3a8,#6d5338)" role="img" aria-label="Brown duck spreading its wings in green water"></div>
<div class="photo abs" style="left:448px;top:665px;background:linear-gradient(160deg,#5a4a35,#2a2118)" role="img" aria-label="Hooded mergansers swimming together"></div>
<div class="photo abs" style="left:771px;top:665px;background:linear-gradient(160deg,#2d5784,#143459)" role="img" aria-label="Loon floating on deep blue water"></div>
<div class="photo abs" style="left:128px;top:987px;background:linear-gradient(160deg,#6b7a48,#3d4a25)" role="img" aria-label="Two cedar waxwings perched in a juniper"></div>
<div class="photo abs" style="left:448px;top:987px;background:linear-gradient(160deg,#5b4a38,#2e251c)" role="img" aria-label="Great horned owl on a pine branch"></div>
<div class="photo abs" style="left:771px;top:987px;background:linear-gradient(160deg,#b89670,#d8d2cc)" role="img" aria-label="Red fox sitting in snow"></div>
<div class="btn-outline abs" style="left:546px;top:1330px">VIEW ALL</div>

<!-- Blogs -->
<section class="blogs-band abs"></section>
<div class="title-rule abs" style="left:0;top:1518px;width:113px"></div>
<h2 class="section-title abs" style="left:126px;top:1499px">Blogs</h2>
<div class="abs" style="left:1020px;top:1510px;display:flex;gap:4px">
  <div class="arrow-box dim"><svg width="8" height="10" viewBox="0 0 8 10"><path d="M6 1 2 5l4 4" stroke="#777" stroke-width="1.6" fill="none"/></svg></div>
  <div class="arrow-box"><svg width="8" height="10" viewBox="0 0 8 10"><path d="M2 1l4 4-4 4" stroke="#222" stroke-width="1.6" fill="none"/></svg></div>
</div>

<div class="abs" style="left:127px;top:1570px;width:425px;height:240px;background:linear-gradient(160deg,#2e4a86,#b98a55 55%,#d9dde8)" role="img" aria-label="Rabbit leaping across snow"></div>
<h3 class="post-title abs" style="left:610px;top:1610px;width:300px;font-size:17px;line-height:24px">Lorem Ipsum is simply dummy text of the printing...</h3>
<p class="abs" style="left:610px;top:1677px;width:400px;font-size:11px;line-height:20px;color:var(--faint)">Lorem Ipsum is simply dummy text of the printing and typesetting in-dustry. Lorem Ipsum has been the industry's standard...</p>
<div class="meta abs" style="left:610px;top:1746px">
  <svg width="13" height="13" viewBox="0 0 14 14"><rect x="1" y="2" width="12" height="11" rx="1" stroke="#8a8a8a" fill="none" stroke-width="1.3"/><path d="M1 5h12M4 0v3M10 0v3" stroke="#8a8a8a" stroke-width="1.3"/></svg>
  31 Mar, 2021<span class="sep"></span><span class="read">READ MORE</span>
</div>

<div class="abs" style="left:127px;top:1831px;width:171px;height:92px;background:linear-gradient(160deg,#3c6aa8,#8f9aa8)" role="img" aria-label="Gull calling with open beak"></div>
<h3 class="post-title abs" style="left:319px;top:1838px;width:240px;font-size:13px;line-height:19px">Lorem Ipsum is simply dummy text of the printing...</h3>
<div class="meta abs" style="left:319px;top:1898px">
  <svg width="13" height="13" viewBox="0 0 14 14"><rect x="1" y="2" width="12" height="11" rx="1" stroke="#8a8a8a" fill="none" stroke-width="1.3"/><path d="M1 5h12M4 0v3M10 0v3" stroke="#8a8a8a" stroke-width="1.3"/></svg>
  31 Mar 2021<span class="sep"></span><span class="read">READ MORE</span>
</div>

<div class="abs" style="left:610px;top:1831px;width:172px;height:92px;background:linear-gradient(160deg,#24487a,#7a3a24)" role="img" aria-label="Harlequin ducks on blue water"></div>
<h3 class="post-title abs" style="left:804px;top:1838px;width:240px;font-size:13px;line-height:19px">Lorem Ipsum is simply dummy text of the printing...</h3>
<div class="meta abs" style="left:804px;top:1898px">
  <svg width="13" height="13" viewBox="0 0 14 14"><rect x="1" y="2" width="12" height="11" rx="1" stroke="#8a8a8a" fill="none" stroke-width="1.3"/><path d="M1 5h12M4 0v3M10 0v3" stroke="#8a8a8a" stroke-width="1.3"/></svg>
  31 Mar 2021<span class="sep"></span><span class="read on">READ MORE</span>
</div>
<div class="btn-outline abs" style="left:546px;top:1966px">VIEW ALL</div>

<!-- Quick inquiry -->
<h2 class="section-title abs" style="left:0;width:1200px;text-align:center;top:2128px">Quick Inquiry</h2>
<div class="field abs" style="left:323px;top:2200px;width:270px;height:33px">
  <svg width="11" height="11" viewBox="0 0 12 12"><circle cx="6" cy="3.5" r="2.6" stroke="#666" fill="none"/><path d="M1 11.5c0-3 2.2-4.5 5-4.5s5 1.5 5 4.5" stroke="#666" fill="none"/></svg>Name</div>
<div class="field abs" style="left:323px;top:2241px;width:270px;height:33px">
  <svg width="12" height="10" viewBox="0 0 12 10"><rect x=".5" y=".5" width="11" height="9" stroke="#666" fill="none"/><path d="M.5 .5l5.5 5 5.5-5" stroke="#666" fill="none"/></svg>Email</div>
<div class="field abs" style="left:323px;top:2282px;width:270px;height:33px">
  <svg width="9" height="12" viewBox="0 0 9 12"><rect x=".5" y=".5" width="8" height="11" rx="1" stroke="#666" fill="none"/><path d="M3 9.5h3" stroke="#666"/></svg>Phone</div>
<div class="field area abs" style="left:607px;top:2200px;width:269px;height:115px">
  <svg width="12" height="12" viewBox="0 0 12 12"><path d="M.5 .5h11v7l-4 4h-7z M7.5 11.5v-4h4" stroke="#666" fill="none"/></svg>How can we help?</div>
<div class="btn-submit abs">SUBMIT</div>

<!-- Footer -->
<div class="brand abs" style="left:128px;top:2516px">Nora Falkett</div>
<p class="abs" style="left:128px;top:2570px;width:440px;font-size:11.5px;line-height:21px;color:var(--text)">Lorem Ipsum is simply dummy text of the printing and typesetting industry. Lorem Ipsum has been the industry's standard dummy text ever since the 1500s, when an unknown printer took</p>

<h4 class="footer-head abs" style="left:691px;top:2500px;font-weight:400">Quick Link</h4>
<ul class="footer-links abs" style="left:691px;top:2539px">
  <li class="on">Home</li><li>About Us</li><li>Photo Gallery</li><li>Blogs</li><li>Contact Us</li>
</ul>

<h4 class="footer-head abs" style="left:894px;top:2500px;font-weight:400">Conatct info</h4>
<ul class="footer-contact abs" style="left:894px;top:2536px">
  <li><svg width="12" height="15" viewBox="0 0 12 15"><path d="M6 0a6 6 0 0 0-6 6c0 4.5 6 9 6 9s6-4.5 6-9a6 6 0 0 0-6-6z" fill="var(--gold)"/><circle cx="6" cy="6" r="2.2" fill="#0e0e0e"/></svg>Out in the wilderness</li>
  <li><svg width="13" height="13" viewBox="0 0 24 24"><path fill="var(--gold)" d="M6.6 10.8a15 15 0 0 0 6.6 6.6l2.2-2.2c.3-.3.7-.4 1-.2 1.1.4 2.3.6 3.6.6.6 0 1 .4 1 1V20c0 .6-.4 1-1 1A17 17 0 0 1 3 4c0-.6.4-1 1-1h3.5c.6 0 1 .4 1 1 0 1.3.2 2.5.6 3.6.1.3 0 .7-.2 1z"/></svg>443-581-2094</li>
  <li><svg width="14" height="10" viewBox="0 0 14 10"><rect width="14" height="10" fill="var(--gold)"/><path d="M0 0l7 6 7-6" stroke="#0e0e0e" stroke-width="1.2" fill="none"/></svg>nora@fernowlpix.com</li>
</ul>

<div class="footer-bar abs">
  <span class="abs" style="left:128px;top:13px;font-size:10px;color:var(--muted)">Copyright © 2021 Nora Falkett. All Rights Reserved</span>
  <div class="socials abs" style="left:973px;top:12px">
    <span class="social-dot" style="border-color:var(--white)"></span><span class="social-dot" style="border-color:var(--gold)"></span><span class="social-dot" style="border-color:var(--white)"></span><span class="social-dot" style="border-color:var(--white)"></span>
  </div>
</div>

</body>
</html>
```